nutrition company business card

I would like to have a business card that has two sides, one being the green color from the Company name on the logo. I am open to ideas and looks that work with my logo. I like the idea of having a negative image of the tree on the green side.

For my information on the card I must have:
Linda Moorcombe
415-872-6041
lindamoorcombe@quellmail.net

This area will need to be updated once I complete my schooling.

Reason: I need to extend my deadline by one day as I have been sick the last week and not had time to review all the new designs. Thank you.

Industry/Entity Type

Nutrition

Requirements
Must have
• I would like to have a business card that has two sides, one being the green color from the Company name on the logo. I am open to ideas and looks that work with my logo. I like the idea of having a negative image of the tree on the green side.
• For my information on the card I must have:
• Linda Moorcombe
• 415-872-6041
• lindamoorcombe@quellmail.net
• This area will need to be updated once I complete my schooling.

```html
<!DOCTYPE html>
<html lang="en">
<head>
<meta charset="utf-8">
<title>Verdant Tables – Business Card, Two Sides</title>
<link rel="stylesheet" href="https://fonts.googleapis.com/css2?family=Quicksand:wght@400;500&family=Roboto+Condensed:wght@700&family=Roboto:wght@400&display=swap">
<style>
  :root {
    --leaf-green: #8cc63f;
    --band-green-deep: #a3cf3c;
    --band-green-soft: #d9e9ae;
    --wave-green: #d3e49a;
    --tagline-grey: #7a7a7a;
    --ink: #231f20;
    --label-grey: #3a3a3a;
    --ring-taupe: #9b9088;
    --card-edge: #c9c9c9;
    --page: #ffffff;
  }
  * { margin: 0; padding: 0; box-sizing: border-box; }
  html, body {
    width: 1200px; height: 429px; overflow: hidden;
    background: var(--page);
  }
  .sheet { position: relative; width: 1200px; height: 429px; }

  .side-label {
    position: absolute; top: 0;
    font-family: "Roboto", Arial, sans-serif;
    font-size: 48px; line-height: 48px; color: var(--label-grey);
    transform: translateX(-50%);
  }
  .side-label--a { left: 249px; }
  .side-label--b { left: 868px; }

  .card { position: absolute; width: 590px; height: 365px; overflow: hidden; }
  .card--a { left: 0; top: 64px; }
  .card--b { left: 608px; top: 64px; height: 364px; outline: 1px solid var(--card-edge); }

  .card__art { position: absolute; inset: 0; width: 100%; height: 100%; }

  .brand {
    position: absolute; left: 0; right: 0; top: 10px;
    text-align: center;
    font-family: "Quicksand", Arial, sans-serif;
  }
  .card--b .brand { top: 13px; }
  .brand__name {
    font-size: 39px; font-weight: 500; color: var(--leaf-green);
    line-height: 44px; letter-spacing: 0.5px;
  }
  .brand__tagline {
    font-size: 19px; font-weight: 400; color: var(--tagline-grey);
    letter-spacing: 2.4px; line-height: 20px;
  }

  .brand-mark {
    position: absolute; left: 24px; top: 117px;
    width: 106px; height: 106px; border-radius: 50%;
    border: 4px solid var(--ring-taupe);
  }
  .card--b .brand-mark { top: 121px; }

  .contact { position: absolute; left: 0; right: 0; top: 0; }
  .contact__name {
    position: absolute; left: 174px; top: 162px;
    font-family: "Roboto Condensed", "Arial Narrow", sans-serif;
    font-weight: 700; font-size: 29px; color: var(--ink); line-height: 32px;
  }
  .contact__phone, .contact__email {
    position: absolute; right: 26px;
    font-family: "Roboto Condensed", "Arial Narrow", sans-serif;
    font-weight: 700; color: var(--ink); text-align: right;
  }
  .contact__phone { top: 191px; font-size: 19px; line-height: 20px; }
  .contact__email { top: 214px; font-size: 18px; line-height: 20px; }
  .card--b .contact { top: 4px; }
</style>
</head>
<body>
<main class="sheet">
  <p class="side-label side-label--a">side A</p>
  <p class="side-label side-label--b">side B</p>

  <!-- Side A: green side -->
  <section class="card card--a" aria-label="Business card, side A">
    <svg class="card__art" viewBox="0 0 533 329" preserveAspectRatio="none" aria-hidden="true">
      <defs>
        <linearGradient id="band-a" x1="0" x2="1" y1="0" y2="0">
          <stop offset="0" stop-color="#d9e9b0"/>
          <stop offset="1" stop-color="#a3cf3c"/>
        </linearGradient>
      </defs>
      <rect width="533" height="329" fill="#ffffff"/>
      <path d="M0,0 H533 V72 C470,58 400,50 320,62 C240,74 180,96 110,92 C60,89 25,78 0,62 Z" fill="#d3e49a"/>
      <rect x="0" y="104" width="533" height="115" fill="url(#band-a)"/>
      <path d="M0,250 C90,226 200,236 300,244 C400,252 470,232 533,226 V329 H0 Z" fill="#d3e49a"/>
    </svg>
    <div class="brand">
      <p class="brand__name">Verdant Tables</p>
      <p class="brand__tagline">healthy eating made easy</p>
    </div>
    <div class="brand-mark" aria-hidden="true"></div>
    <div class="contact">
      <p class="contact__name">Linda Moorcombe</p>
      <p class="contact__phone">415-872-6041</p>
      <p class="contact__email">lindamoorcombe@quellmail.net</p>
    </div>
  </section>

  <!-- Side B: white side -->
  <section class="card card--b" aria-label="Business card, side B">
    <svg class="card__art" viewBox="0 0 533 329" preserveAspectRatio="none" aria-hidden="true">
      <defs>
        <linearGradient id="band-b" x1="0" x2="1" y1="0" y2="0">
          <stop offset="0" stop-color="#dbe9b2"/>
          <stop offset="0.55" stop-color="#ffffff"/>
          <stop offset="1" stop-color="#ffffff"/>
        </linearGradient>
      </defs>
      <rect width="533" height="329" fill="#ffffff"/>
      <path d="M0,88 C110,90 220,82 320,68 C410,56 480,52 533,60 V106 H0 Z" fill="#d3e49a"/>
      <rect x="0" y="106" width="533" height="118" fill="url(#band-b)"/>
      <path d="M0,224 H533 V266 C460,252 370,244 270,252 C170,260 80,264 0,246 Z" fill="#d3e49a"/>
    </svg>
    <div class="brand">
      <p class="brand__name">Verdant Tables</p>
      <p class="brand__tagline">healthy eating made easy</p>
    </div>
    <div class="brand-mark" aria-hidden="true"></div>
    <div class="contact">
      <p class="contact__name">Linda Moorcombe</p>
      <p class="contact__phone">415-872-6041</p>
      <p class="contact__email">lindamoorcombe@quellmail.net</p>
    </div>
  </section>
</main>
</body>
</html>
```